Business card design for my trucking company

I would like a business card designed for my new trucking company. Please use my logo. the rest of the design is up to you. i would like my clients to say wow when they see the card. Im looking forward to seeing your designs

Target Market(s)

Industry/Entity Type

Trucking Company

Contact Information for Business Card

Marcus Tillbrook President
518-555-0147
ridgelinehaulingcompany@postvane.com

Font styles to use
Serif

Requirements
Must have
• my logo, name and number. we are located in Millbrook Falls New York. the rest is up to you
Nice to have
• up to you
Should not have
• none

```html
<!DOCTYPE html>
<html lang="en">
<head>
<meta charset="utf-8">
<title>Ridgeline Hauling &amp; Logistics – Business Card</title>
<link href="https://fonts.googleapis.com/css2?family=Poppins:wght@400;500;800&display=swap" rel="stylesheet">
<style>
  :root {
    --brand-red: #e3222b;
    --ink-black: #141416;
    --paper: #ffffff;
    --stage: #e9e9ec;
    --sky-top: #cfc8d6;
    --sky-mid: #f0d9d6;
    --road: #8d8379;
    --ridge: #5e5a6e;
  }
  * { box-sizing: border-box; margin: 0; padding: 0; }
  html, body { width: 1200px; height: 800px; overflow: hidden; }
  body {
    background: var(--stage);
    font-family: "Poppins", Arial, sans-serif;
    position: relative;
  }
  .card {
    position: absolute;
    width: 540px;
    height: 309px;
    border-radius: 18px;
    background: var(--paper);
    overflow: hidden;
    box-shadow: 0 14px 30px rgba(0,0,0,.18);
    top: 245px;
  }
  .card--front { left: 30px; }
  .card--back { left: 630px; }

  /* Brand name (text only) */
  .brand-name {
    color: var(--brand-red);
    font-weight: 800;
    text-transform: uppercase;
    line-height: 1;
  }
  .brand-name__main { display: block; font-size: 46px; letter-spacing: 1px; }
  .brand-name__sub { display: block; font-size: 13.5px; letter-spacing: 1.2px; margin-top: 6px; }

  .card--front .brand-name {
    position: absolute;
    left: 0; right: 0; top: 112px;
    text-align: center;
  }
  .front-band { position: absolute; left: 0; bottom: 0; width: 540px; height: 40px; }

  /* Back */
  .photo-area { position: absolute; inset: 0; }
  .card--back .brand-name {
    position: absolute;
    left: 28px; top: 92px;
  }
  .card--back .brand-name__main { font-size: 40px; }
  .card--back .brand-name__sub { font-size: 11.5px; }

  .band-shapes { position: absolute; left: 0; top: 0; width: 540px; height: 309px; }

  .person {
    position: absolute;
    left: 24px; top: 244px;
    color: var(--paper);
    text-transform: uppercase;
    line-height: 1.05;
  }
  .person__name { font-weight: 800; font-size: 19px; letter-spacing: .3px; }
  .person__title { font-weight: 400; font-size: 13px; letter-spacing: .5px; }

  .contact {
    position: absolute;
    right: 16px; top: 196px;
    color: var(--paper);
    text-align: right;
    font-size: 11.5px;
    line-height: 1.55;
  }
  .contact__row { display: flex; align-items: center; justify-content: flex-end; gap: 6px; }
  .contact__icon { width: 11px; height: 11px; flex: none; }

  .location {
    position: absolute;
    left: 258px; right: 16px; top: 262px;
    text-align: center;
    color: var(--ink-black);
    font-size: 14px;
    letter-spacing: 3px;
    text-transform: uppercase;
  }
</style>
</head>
<body>

  <section class="card card--front" aria-label="Card front">
    <div class="brand-name">
      <span class="brand-name__main">Ridgeline</span>
      <span class="brand-name__sub">Hauling &amp; Logistics Inc.</span>
    </div>
    <svg class="front-band" viewBox="0 0 540 40" aria-hidden="true">
      <polygon points="230,22 540,22 540,40 212,40" fill="var(--brand-red)"/>
    </svg>
  </section>

  <section class="card card--back" aria-label="Card back">
    <svg class="photo-area" viewBox="0 0 540 309" role="img" aria-label="Photo of a white semi truck driving on a desert highway at sunset with mountains behind">
      <defs>
        <linearGradient id="sky" x1="0" y1="0" x2="0" y2="1">
          <stop offset="0" stop-color="var(--sky-top)"/>
          <stop offset=".55" stop-color="var(--sky-mid)"/>
          <stop offset=".72" stop-color="var(--ridge)"/>
          <stop offset="1" stop-color="var(--road)"/>
        </linearGradient>
      </defs>
      <rect width="540" height="309" fill="url(#sky)"/>
    </svg>

    <div class="brand-name">
      <span class="brand-name__main">Ridgeline</span>
      <span class="brand-name__sub">Hauling &amp; Logistics Inc.</span>
    </div>

    <svg class="band-shapes" viewBox="0 0 540 309" aria-hidden="true">
      <polygon points="240,188 540,188 540,238 222,238" fill="var(--ink-black)"/>
      <rect x="0" y="238" width="540" height="71" fill="var(--paper)"/>
      <polygon points="0,226 246,226 226,309 0,309" fill="var(--brand-red)"/>
    </svg>

    <div class="person">
      <div class="person__name">Marcus Tillbrook</div>
      <div class="person__title">President</div>
    </div>

    <div class="contact">
      <div class="contact__row">518-555-0147
        <svg class="contact__icon" viewBox="0 0 12 12" aria-hidden="true"><circle cx="6" cy="6" r="6" fill="var(--brand-red)"/><path d="M4 3.2l1 1.4-.6.7c.4.9 1 1.5 1.9 1.9l.7-.6 1.4 1-.5 1.1C5.6 8.6 3.4 6.4 3 4.1z" fill="#fff"/></svg>
      </div>
      <div class="contact__row">ridgelinehaulingcompany@postvane.com
        <svg class="contact__icon" viewBox="0 0 12 12" aria-hidden="true"><circle cx="6" cy="6" r="6" fill="var(--brand-red)"/><rect x="3" y="4" width="6" height="4.2" fill="#fff"/><path d="M3 4l3 2.3L9 4" stroke="var(--brand-red)" stroke-width=".8" fill="none"/></svg>
      </div>
    </div>

    <div class="location">Millbrook Falls New York</div>
  </section>

</body>
</html>
```